International Manufacturing Business Needs A Heavy Hitting Wordpress Design!

We need wordpress template designs for a new website for our UK based International company Tolvane Engineering Ltd. We manufacture and supply steel security doors and window units. We would like designs that feature the black and yellow industrial "stripes" that can be seen at our current site www.tolvadoors.com. The final design should communicate strength, power and weight to represent the quality of the products and the security that they provide.

It feels like we need 3 different types of page to be able to be created as per the current website at www.tolvasecuredoors.com.

Homepage
Products/Accessories
Leadtimes/Downloads/Contact

It may be that 3 different page types can be created with one template. I'm totally open to this.

I don't like the way that the site currently handles product images, nobody wants to click on even thumbnail to see the product. http://tolvasecuredoors.com/products/personnel-doors/

Totally open to suggestions on layout to enable the feeling outlined in the brief above.

Please ask if anything is not clear or you need answers to drill down on specifics.

Sick

Target Market(s)

Businesses that buy steel doors

Font styles to use
Sans Serif
Other font styles liked:
• Copperplate Gothic Bold - For Company Name but we are open to suggestions

Colors

Designer to choose colors to be used in the design.

Requirements
Must have
• Professional looking, clean design
• Conveys strength, power and weight to represent the quality of the products, the characteristics of steel and the security that they provide.
• Incorporates black and yellow stripes of our branding
• Ability to create pages with content as seen at www.tolvasecuredoors.com
• A better way of showing the product images
Nice to have
• If possible. a design that gives off the feeling that not only do we supply the products we also make them in house too. I don't know what this looks like but a way of differentiating between a supply only business and one that manufacturers the product too.
Should not have
• We don't like the current thumbnail method of showing the product images

```html
<!DOCTYPE html>
<html lang="en">
<head>
<meta charset="utf-8">
<title>Tolvane Engineering Ltd – Steel Security Doors</title>
<link rel="stylesheet" href="https://fonts.googleapis.com/css2?family=Exo+2:wght@400;500;600;700&family=Open+Sans:wght@400;600&display=swap">
<style>
:root{
  --yellow:#f2e617;
  --ink:#111;
  --bg-header:#1d1d1d;
  --bg-dark:#1a1a1a;
  --bg-mid:#2a2a2a;
  --card:#3a3a3a;
  --text:#e6e6e6;
  --muted:#bdbdbd;
  --footer:#141414;
}
*{box-sizing:border-box;margin:0;padding:0}
html,body{width:1200px;height:3734px;overflow:hidden}
body{background:var(--bg-dark);color:var(--text);font-family:"Open Sans",Arial,sans-serif;position:relative}
.abs{position:absolute}
h2{font-family:"Exo 2",Arial,sans-serif;font-weight:500;color:#fff;text-align:center}
.rule{display:block;width:70px;height:4px;background:var(--yellow);margin:14px auto 0;border-radius:2px}
.btn{display:inline-block;background:var(--yellow);color:var(--ink);font-family:"Exo 2",Arial,sans-serif;font-weight:600;font-size:15px;padding:0 32px;height:30px;line-height:30px;border-radius:15px}

/* header */
.site-header{left:0;top:0;width:1200px;height:135px;background:var(--bg-header)}
.brand{left:130px;top:36px;display:flex;align-items:center;gap:14px}
.brand-mark{width:40px;height:58px;background:var(--yellow)}
.brand-name{font-family:"Exo 2",Arial,sans-serif;font-weight:700;font-size:26px;line-height:28px;color:#fff;text-transform:uppercase;letter-spacing:1px}
.contact-bar{right:130px;top:52px;display:flex;align-items:center;gap:26px;font-size:15px}
.contact-bar span{display:flex;align-items:center;gap:10px}
.contact-bar .phone{color:var(--yellow)}
.menu{width:22px;height:16px;display:flex;flex-direction:column;justify-content:space-between}
.menu i{height:3px;background:#fff;display:block}

/* hero */
.hero{left:0;top:135px;width:1200px;height:610px;background:linear-gradient(180deg,#5c88ad 0%,#8eb0c9 35%,#6b4a3a 55%,#3f4a3a 78%,#1a1d1a 100%)}
.hero-arrow{top:300px;width:26px;height:26px;border-radius:50%;display:flex;align-items:center;justify-content:center}
.dots{left:576px;top:570px;display:flex;gap:8px}
.dots i{width:7px;height:7px;border-radius:50%;background:#777;display:block}
.dots i.on{background:var(--yellow)}

/* what we do */
.what{left:0;top:745px;width:1200px;height:570px;background:var(--bg-dark)}
.what h2{margin-top:60px;font-size:30px}
.what p{text-align:center;font-size:15px;line-height:24px;color:var(--text)}
.intro{width:700px;margin:30px auto 0}
.intro p+p{margin-top:14px}
.what .cta{text-align:center;margin-top:16px}
.service{top:293px;width:423px;height:175px;background:var(--card);border-radius:6px;padding:24px 30px}
.service h3{font-family:"Exo 2",Arial,sans-serif;font-weight:500;font-size:20px;color:#fff}
.service p{text-align:left;font-size:14px;line-height:20px;width:230px;margin-top:10px}
.service .more{font-size:14px;margin-top:12px;display:flex;align-items:center;gap:6px}
.service .thumb{right:20px;top:8px;width:100px;height:160px;background:linear-gradient(180deg,#5a5a5a,#2d2d2d);border-right:14px solid var(--yellow)}

/* featured products */
.featured{left:0;top:1315px;width:1200px;height:610px;background:var(--bg-mid)}
.featured h2{margin-top:52px;font-size:34px}
.tabs{left:0;top:130px;width:1200px;display:flex;justify-content:center;gap:0;font-size:14px}
.tabs span{padding:0 20px;border-left:1px solid #666}
.tabs span:first-child{border:none;color:var(--yellow);text-decoration:underline}
.tab-arrows{right:115px;top:128px;display:flex;gap:4px}
.tab-arrows i{width:17px;height:17px;border-radius:50%;display:block;background:#ddd}
.tab-arrows i+i{background:var(--yellow)}
.products{left:112px;top:190px;display:flex;gap:6px}
.product{width:240px;height:295px;background:var(--card)}
.product .photo{width:230px;height:245px;margin:5px}
.product p{text-align:center;font-size:14px;line-height:40px;margin-top:-2px}
.featured .cta{left:0;top:540px;width:1200px;text-align:center}

/* downloads */
.downloads{left:0;top:1925px;width:1200px;height:550px;background:var(--bg-dark)}
.downloads h2{margin-top:52px;font-size:34px}
.downloads .sub{text-align:center;font-family:"Exo 2",Arial,sans-serif;font-size:17px;margin-top:14px}
.downloads .sub .rule{margin-top:10px}
.brochures{left:125px;top:172px;font-size:14px;line-height:35px}
.diagrams{left:148px;top:282px;font-size:14px;line-height:27px;list-style:none}
.diagrams li::before{content:"";display:inline-block;width:6px;height:6px;border-radius:50%;background:#fff;margin-right:14px;vertical-align:middle}
.diagrams li.active{color:var(--yellow);text-decoration:underline}
.diagrams li.active::before{background:var(--yellow)}
.diagrams .pair span+span{margin-left:24px}
.downloads .cta{left:125px;top:435px}
.pdf-art{left:820px;top:188px;width:265px;height:258px;background:linear-gradient(160deg,#f4f4f4 0%,#d8d8d8 70%,#b03030 100%);border-radius:4px}

/* latest products */
.latest{left:0;top:2475px;width:1200px;height:610px;background:var(--bg-mid)}
.latest h2{margin-top:52px;font-size:34px}
.latest .copy{left:122px;top:222px;width:260px}
.latest h3{font-family:"Exo 2",Arial,sans-serif;font-weight:500;font-size:19px;color:#fff;padding-bottom:8px;border-bottom:2px solid var(--text);display:inline-block}
.latest .copy p{font-size:14px;line-height:20px;margin:22px 0 12px}
.slide{left:425px;top:155px;width:657px;height:348px;border-radius:8px;background:linear-gradient(90deg,#d9dde0 0%,#7f878d 30%,#3e4348 55%,#5d636a 100%)}
.slide-arrow{top:290px;width:40px;height:60px;background:#111;display:flex;align-items:center;justify-content:center}

/* newsletter */
.newsletter{left:0;top:3085px;width:1200px;height:220px;background:var(--bg-dark)}
.newsletter h2{margin-top:62px;font-size:24px}
.newsletter .rule{width:60px;margin-top:8px}
.signup{left:340px;top:106px;display:flex}
.signup .field{width:382px;height:32px;background:#3a3a3a;border-radius:16px 0 0 16px;font-size:13px;line-height:32px;padding-left:22px;color:#ddd}
.signup .send{width:130px;height:32px;background:var(--yellow);color:var(--ink);border-radius:0 16px 16px 0;font-size:13px;line-height:32px;text-align:center}

/* footer */
.site-footer{left:0;top:3305px;width:1200px;height:380px;background:linear-gradient(180deg,#1e1e1e,#0e0e0e)}
.foot-brand{left:115px;top:82px;display:flex;align-items:center;gap:12px}
.foot-brand .brand-mark{width:32px;height:48px}
.foot-brand .brand-name{font-size:21px;line-height:23px}
.foot-about{left:120px;top:160px;width:240px;font-size:13px;line-height:17px}
.badges{left:120px;top:245px;display:flex;gap:12px}
.badges i{display:block;width:72px;height:44px;background:#d8d8d8}
.badges i:last-child{background:#8a5a2a}
.foot-col{top:88px}
.foot-col h4{font-family:"Exo 2",Arial,sans-serif;font-weight:500;font-size:16px;color:#fff}
.foot-col h4::after{content:"";display:block;width:70px;height:2px;background:#fff;margin-top:12px}
.foot-col ul{list-style:none;margin-top:24px;font-size:13px;line-height:19px}
.links li::before{content:"•";margin-right:10px}
.address li{display:flex;gap:10px}
.qc{display:grid;grid-template-columns:112px 112px;gap:8px 6px;margin-top:26px}
.qc div{background:#fff;color:#333;font-size:11px;height:20px;line-height:20px;padding-left:5px}
.qc .msg{grid-column:span 2;height:50px}
.qc .send{grid-column:2;background:var(--yellow);border-radius:10px;text-align:center;padding:0;font-weight:600}

.legal{left:0;top:3685px;width:1200px;height:49px;background:#fff;color:#222}
.legal p{position:absolute;left:120px;top:16px;font-size:13px;font-weight:600}
.socials{position:absolute;right:115px;top:13px;display:flex;gap:8px}
.socials i{display:block;width:23px;height:23px;border-radius:50%;background:#222}
</style>
</head>
<body>

<header class="site-header abs">
  <div class="brand abs"><span class="brand-mark"></span><span class="brand-name">Tolvane<br>Engineering Ltd.</span></div>
  <div class="contact-bar abs">
    <span><svg width="20" height="20" viewBox="0 0 20 20"><circle cx="10" cy="10" r="9" fill="none" stroke="#fff" stroke-width="1.6"/><rect x="5" y="6.5" width="10" height="7" fill="none" stroke="#fff" stroke-width="1.4"/><path d="M5 7l5 4 5-4" fill="none" stroke="#fff" stroke-width="1.4"/></svg>sales@tolvadoors.com</span>
    <span class="phone"><svg width="20" height="20" viewBox="0 0 20 20"><circle cx="10" cy="10" r="9" fill="none" stroke="#f2e617" stroke-width="1.6"/><path d="M7 5.5l2 2-1 1.5c.6 1.3 1.6 2.3 2.9 2.9l1.5-1 2 2-1.3 1.6C9.5 14 6 10.5 5.5 6.8z" fill="#f2e617"/></svg>+44 (0)1632 960 300</span>
    <span class="menu"><i></i><i></i><i></i></span>
  </div>
</header>

<section class="hero abs" role="img" aria-label="Photograph of a large tudor-style house with red tiled roof under a blue evening sky">
  <span class="hero-arrow abs" style="left:48px;background:#fff"><svg width="10" height="10" viewBox="0 0 10 10"><path d="M7 1L3 5l4 4" fill="none" stroke="#111" stroke-width="2"/></svg></span>
  <span class="hero-arrow abs" style="right:48px;background:var(--yellow)"><svg width="10" height="10" viewBox="0 0 10 10"><path d="M3 1l4 4-4 4" fill="none" stroke="#111" stroke-width="2"/></svg></span>
  <div class="dots abs"><i class="on"></i><i></i><i></i><i></i></div>
</section>

<section class="what abs">
  <h2>What We Do...<span class="rule"></span></h2>
  <div class="intro">
    <p>Tolvane security doors combine a high level of security with exceptional value.</p>
    <p>Our superior quality and proven reliability has made us the first choice for a wide range of companies no matter what their requirement or application.</p>
  </div>
  <div class="cta"><span class="btn">View More</span></div>
  <article class="service abs" style="left:168px">
    <h3>Security Doors</h3>
    <p>Affordable steel personnel doors that do not compromise on quality or security</p>
    <div class="more">Read More.. <svg width="12" height="12" viewBox="0 0 12 12"><circle cx="6" cy="6" r="5" fill="none" stroke="#ddd"/><path d="M5 3.5L7.5 6 5 8.5" fill="none" stroke="#ddd"/></svg></div>
    <div class="thumb abs" role="img" aria-label="Brochure cover showing a red steel security door"></div>
  </article>
  <article class="service abs" style="left:615px">
    <h3>Fire Exit Doorst</h3>
    <p>The same high quality Tolvane door available with a range of fire exit hardware</p>
    <div class="more">Read More.. <svg width="12" height="12" viewBox="0 0 12 12"><circle cx="6" cy="6" r="5" fill="none" stroke="#ddd"/><path d="M5 3.5L7.5 6 5 8.5" fill="none" stroke="#ddd"/></svg></div>
    <div class="thumb abs" role="img" aria-label="Brochure cover showing a red steel fire exit door"></div>
  </article>
</section>

<section class="featured abs">
  <h2>Freature Product<span class="rule"></span></h2>
  <nav class="tabs abs"><span>All</span><span>Personnel Doors</span><span>Fire Exit Doors</span><span>Blank Doors</span><span>Technical Videos</span><span>Accessories</span></nav>
  <div class="tab-arrows abs"><i></i><i></i></div>
  <div class="products abs">
    <div class="product"><div class="photo" role="img" aria-label="Grey steel door with anti-vandal handle shroud" style="background:linear-gradient(160deg,#8a939b,#4e565d)"></div><p>Anti-Vandal Shroud</p></div>
    <div class="product"><div class="photo" role="img" aria-label="Worker spray painting a door in a paint booth" style="background:linear-gradient(160deg,#c9d3c2,#5d6b55)"></div><p>Paint Finish</p></div>
    <div class="product"><div class="photo" role="img" aria-label="Grey steel cloaking frame panel on white" style="background:linear-gradient(160deg,#ffffff,#c4c4c4)"></div><p>Cloaking Frames</p></div>
    <div class="product"><div class="photo" role="img" aria-label="Blue steel door with hydraulic closer and cream panel" style="background:linear-gradient(160deg,#2f6fb3,#163e6d)"></div><p>Hydraulic Closers</p></div>
  </div>
  <div class="cta abs"><span class="btn">View More</span></div>
</section>

<section class="downloads abs">
  <h2>Downloads</h2>
  <div class="sub">Brochures<span class="rule"></span></div>
  <div class="brochures abs">
    <p>10-Point Locking Steel Personnel Doors Brochure (click to download) (1.67 MB bytes)</p>
    <p>Steel Fire Exit Doors Brochure (click to download) (1.53 MB bytes)</p>
    <p>Anti-Vandal Steel Shutters and Glazing Units Brochure (click to download) (1.9 MB bytes)</p>
  </div>
  <ul class="diagrams abs">
    <li class="active">Technical Diagrams - Doors - Overview</li>
    <li>Technical Diagrams - Doors - Frame Profile</li>
    <li>Technical Diagrams - Doors - Fixing Points</li>
    <li class="pair"><span>Door Threshold Diagrams</span><span>• &nbsp;Vision Panels</span></li>
    <li class="pair"><span>Maintenance</span><span>• &nbsp;Fitting Instructions</span></li>
  </ul>
  <div class="cta abs"><span class="btn">View More</span></div>
  <div class="pdf-art abs" role="img" aria-label="Illustration of a PDF document file"></div>
</section>

<section class="latest abs">
  <h2>Our Latest Products<span class="rule"></span></h2>
  <div class="copy abs">
    <h3>Anti-Vandal Shroud</h3>
    <p>Tolvane Engineering's anti-vandal shroud has been designed to offer increased security protection for the standard 10-point locking personnel door.</p>
    <span class="btn">View More</span>
  </div>
  <div class="slide abs" role="img" aria-label="Close-up of a grey steel door edge with multi-point locks and lever handle"></div>
  <span class="slide-arrow abs" style="left:405px;border-radius:0 30px 30px 0;width:56px;left:405px"><svg width="14" height="14" viewBox="0 0 14 14"><path d="M9 2L4 7l5 5" fill="none" stroke="#fff" stroke-width="2.4"/></svg></span>
  <span class="slide-arrow abs" style="left:1046px;border-radius:30px 0 0 30px;width:56px"><svg width="14" height="14" viewBox="0 0 14 14"><path d="M5 2l5 5-5 5" fill="none" stroke="#fff" stroke-width="2.4"/></svg></span>
</section>

<section class="newsletter abs">
  <h2>Join The Newletter<span class="rule"></span></h2>
  <div class="signup abs"><span class="field">Email here</span><span class="send">Subscribe</span></div>
</section>

<footer class="site-footer abs">
  <div class="foot-brand abs"><span class="brand-mark"></span><span class="brand-name">Tolvane<br>Engineering Ltd.</span></div>
  <p class="foot-about abs">Lorem Ipsum is simply dummy text the printing and ypesetting industry has been the industry's standard dummy...</p>
  <div class="badges abs"><i></i><i></i><i></i></div>
  <div class="foot-col abs" style="left:408px">
    <h4>Quick Link</h4>
    <ul class="links"><li>Home</li><li>Products</li><li>Accessories</li><li>Delivery &amp; Lead Times</li><li>Downloads</li><li>Contact</li></ul>
  </div>
  <div class="foot-col abs" style="left:630px">
    <h4>Address</h4>
    <ul class="address">
      <li><svg width="10" height="14" viewBox="0 0 10 14"><path d="M5 0a5 5 0 00-5 5c0 4 5 9 5 9s5-5 5-9a5 5 0 00-5-5z" fill="#fff"/><circle cx="5" cy="5" r="2" fill="#111"/></svg><span>Marlow Ridge, Eastholme,<br>Hull, HU9 4ZX<br>Zip: 40871</span></li>
      <li><svg width="10" height="12" viewBox="0 0 10 12"><path d="M1 1l3 1-1 2c.6 1.6 1.7 2.8 3 3.5l1.5-1 2.5 2-1 2C4 10 1 6 1 1z" fill="#fff"/></svg>+44 (0)1632 960 300</li>
      <li><svg width="12" height="10" viewBox="0 0 12 10"><rect x="0" y="1" width="12" height="8" fill="#fff"/><path d="M0 1l6 4 6-4" fill="none" stroke="#111"/></svg>sales@tolvadoors.com</li>
    </ul>
  </div>
  <div class="foot-col abs" style="left:848px">
    <h4>Quick Contact</h4>
    <div class="qc"><div>Name</div><div>Phone</div><div class="msg">Message</div><div class="send">SEND</div></div>
  </div>
</footer>

<div class="legal abs">
  <p>Privacy policy - Legal mentions - Terms and Conditions</p>
  <div class="socials"><i></i><i></i><i></i><i></i><i></i></div>
</div>

</body>
</html>
```